Harbor Total Recovery Tradeshow Booth Design

We need a tradeshow booth design for a 10x20 booth. We are a COMMERCIAL ONLY disaster restoration company focusing on water and flood restoration, fire and smoke remediation, mold and biohazard, structural repair and asset protection.

These are the links to the booth we need graphics designed for. The spec sheets for them are also in the attachments.
https://www.boothvexa.com/Corvina-Helix-Swift-Frame-p/corvina.htm?CartID=2
https://www.boothvexa.com/Tidara-52-Counter-p/tdc-52.htm?CartID=1
https://www.boothvexa.com/6ft-Stretch-Table-Cover-p/tbl-6-stretch.htm?CartID=5

Target Market(s)

Real Estate, Educational Facilities, Hospitality Facilities, Medical Facilities

Industry/Entity Type

Construction

Requirements
Must have
• Our logo. The colors from the attached presentation. Pictures of COMMERCIAL ONLY facilities and losses (can use some from attached presentation). Our services (water and flood, fire and smoke, mold and biohazard, structural repair, asset protection). Our slogan (Exceeding your expectations when you need it most).
Nice to have
• Include the above
Should not have
• Do not include anything residential looking at all (no pictures). Do not include the case studies on the pictures.

```html
<!DOCTYPE html>
<html lang="en">
<head>
<meta charset="utf-8">
<title>Harbor Total Recovery – Tradeshow Booth Graphics</title>
<link href="https://fonts.googleapis.com/css2?family=Raleway:wght@300;400;600;700;800&display=swap" rel="stylesheet">
<style>
  :root{
    --teal:#426877;
    --orange:#f47b2a;
    --white:#ffffff;
    --grey:#d9d9d9;
    --ink:#3d5f6e;
    --stage:#000000;
  }
  *{box-sizing:border-box;margin:0;padding:0}
  html,body{width:1200px;height:640px;overflow:hidden;background:var(--stage)}
  body{font-family:'Raleway',Arial,sans-serif;position:relative}

  .panel{position:absolute;top:131px;height:378px;overflow:hidden}
  .panel--white{background:var(--white)}
  .panel--teal{background:var(--teal)}

  /* photo banner */
  .brand{position:absolute;top:17px;left:0;right:0;text-align:center;
    color:var(--orange);font-weight:800;font-size:11px;letter-spacing:.3px;text-transform:uppercase;line-height:1.15}
  .photo{position:absolute;left:0;right:0;top:17%;height:58%;
    clip-path:polygon(0 19%,100% 0,100% 100%,0 100%)}
  .photo--roof{background:linear-gradient(160deg,#5f5348 0%,#8b7660 45%,#6b5d4f 100%)}
  .photo--flood{background:linear-gradient(180deg,#8795a6 0%,#6b7f7c 35%,#4a5e3c 60%,#7a6a4f 100%)}
  .photo--gym{background:linear-gradient(180deg,#d7dbe2 0%,#9aa3b3 30%,#b98a58 65%,#2f4c96 100%)}
  .photo--chart{background:linear-gradient(150deg,#f1f4f8 0%,#d3ddea 50%,#5f86c4 100%)}
  .accents{position:absolute;inset:0;width:100%;height:100%}
  .band{position:absolute;left:0;right:0;top:75%;height:3.2%;background:var(--orange)}
  .site{position:absolute;left:0;right:0;text-align:center;color:var(--ink);font-size:10px;font-weight:400}
  .panel--white .site{top:91.2%}
  .dashes{position:absolute;top:95.6%;left:50%;transform:translateX(-50%);display:flex;gap:4px}
  .dashes span{width:19px;height:2px}
  .dashes span:nth-child(1){background:var(--teal)}
  .dashes span:nth-child(2){background:#ececec}
  .dashes span:nth-child(3){background:var(--orange)}

  /* slogan banner */
  .panel--teal .site{color:var(--white);top:2%}
  .slogan{position:absolute;left:12%;right:12%;top:42%;height:16%;
    border:1px solid var(--orange);display:flex;flex-direction:column;align-items:center;justify-content:center;color:var(--white)}
  .slogan__lead{font-size:6px;font-weight:400}
  .slogan__key{font-size:10px;font-weight:700;line-height:1.1}
  .slogan__tail{font-size:5.5px;font-weight:700;color:var(--teal);background:var(--white);padding:1px 5px;border-radius:2px}
  .quote{position:absolute;color:var(--orange);font-weight:800;font-size:34px;line-height:1;font-family:Georgia,serif}
  .quote--open{left:-5px;top:-18px}
  .quote--close{right:-5px;bottom:-30px}
  .slogan .quote{background:none}

  /* services banner */
  .services__frame{position:absolute;left:7%;right:8%;top:3%;height:28%;border:1px solid var(--orange);
    display:flex;flex-direction:column;justify-content:flex-end;padding:0 0 8px 8px;color:var(--orange)}
  .services__our{font-weight:300;font-size:14px;line-height:1.1}
  .services__title{font-weight:700;font-size:14px;line-height:1.1}
  .services__list{position:absolute;left:8%;right:4%;top:38.5%;list-style:none}
  .services__list li{display:flex;align-items:flex-start;gap:5px;color:var(--white);font-size:7.4px;font-weight:700;
    text-transform:uppercase;line-height:1.3;height:24px}
  .services__list b{flex:none;width:6px;height:6px;background:var(--orange);color:var(--white);font-size:4.5px;
    display:flex;align-items:center;justify-content:center;margin-top:1px}
  .panel--services .site{top:92.6%;bottom:auto}
</style>
</head>
<body>

<!-- banner 1 -->
<section class="panel panel--white" style="left:38px;width:172px">
  <div class="brand">Harbor Total Recovery</div>
  <div class="photo photo--roof" role="img" aria-label="Commercial roof damage after a storm"></div>
  <svg class="accents" viewBox="0 0 100 100" preserveAspectRatio="none" aria-hidden="true">
    <polygon points="0,12.3 60,19.5 0,25" fill="var(--teal)"/>
    <polygon points="100,12.3 100,15 78,16.7" fill="var(--teal)"/>
    <polygon points="0,25 100,14.6 100,16.4 0,26.3" fill="var(--orange)"/>
    <polygon points="0,26.3 100,16.4 100,17 0,28" fill="var(--grey)"/>
  </svg>
  <div class="band"></div>
  <p class="site">harbortotalrecovery.com</p>
  <div class="dashes"><span></span><span></span><span></span></div>
</section>

<!-- banner 2 -->
<section class="panel panel--teal" style="left:217px;width:116px">
  <p class="site">harbortotalrecovery.com</p>
  <div class="slogan">
    <span class="quote quote--open">“</span>
    <span class="slogan__lead">Exceeding your</span>
    <span class="slogan__key">EXPECTATIONS</span>
    <span class="slogan__tail">when you need it most.</span>
    <span class="quote quote--close">”</span>
  </div>
</section>

<!-- banner 3 -->
<section class="panel panel--white" style="left:339px;width:195px">
  <div class="brand">Harbor Total Recovery</div>
  <div class="photo photo--flood" role="img" aria-label="Aerial view of a flooded city district"></div>
  <svg class="accents" viewBox="0 0 100 100" preserveAspectRatio="none" aria-hidden="true">
    <polygon points="0,12.3 60,19.5 0,25" fill="var(--teal)"/>
    <polygon points="100,12.3 100,15 78,16.7" fill="var(--teal)"/>
    <polygon points="0,25 100,14.6 100,16.4 0,26.3" fill="var(--orange)"/>
    <polygon points="0,26.3 100,16.4 100,17 0,28" fill="var(--grey)"/>
  </svg>
  <div class="band"></div>
  <p class="site">harbortotalrecovery.com</p>
  <div class="dashes"><span></span><span></span><span></span></div>
</section>

<!-- banner 4 -->
<section class="panel panel--teal panel--services" style="left:541px;width:117px">
  <div class="services__frame">
    <span class="services__our">OUR</span>
    <span class="services__title">SERVICES</span>
  </div>
  <ul class="services__list">
    <li><b>1</b>Water and flood restoration</li>
    <li><b>2</b>Fire and smoke restoration</li>
    <li><b>3</b>Mold remediation</li>
    <li><b>4</b>Structural repair</li>
    <li><b>5</b>Asset management</li>
  </ul>
  <p class="site">harbortotalrecovery.com</p>
</section>

<!-- banner 5 -->
<section class="panel panel--white" style="left:666px;width:195px">
  <div class="brand">Harbor Total Recovery</div>
  <div class="photo photo--gym" role="img" aria-label="School gymnasium with water-damaged buckled floor"></div>
  <svg class="accents" viewBox="0 0 100 100" preserveAspectRatio="none" aria-hidden="true">
    <polygon points="0,12.3 60,19.5 0,25" fill="var(--teal)"/>
    <polygon points="100,12.3 100,15 78,16.7" fill="var(--teal)"/>
    <polygon points="0,25 100,14.6 100,16.4 0,26.3" fill="var(--orange)"/>
    <polygon points="0,26.3 100,16.4 100,17 0,28" fill="var(--grey)"/>
  </svg>
  <div class="band"></div>
  <p class="site">harbortotalrecovery.com</p>
  <div class="dashes"><span></span><span></span><span></span></div>
</section>

<!-- banner 6 -->
<section class="panel panel--teal" style="left:866px;width:117px">
  <p class="site">harbortotalrecovery.com</p>
  <div class="slogan">
    <span class="quote quote--open">“</span>
    <span class="slogan__lead">Exceeding your</span>
    <span class="slogan__key">EXPECTATIONS</span>
    <span class="slogan__tail">when you need it most.</span>
    <span class="quote quote--close">”</span>
  </div>
</section>

<!-- banner 7 -->
<section class="panel panel--white" style="left:990px;width:173px">
  <div class="brand">Harbor Total Recovery</div>
  <div class="photo photo--chart" role="img" aria-label="Hand reviewing printed charts and reports"></div>
  <svg class="accents" viewBox="0 0 100 100" preserveAspectRatio="none" aria-hidden="true">
    <polygon points="0,12.3 60,19.5 0,25" fill="var(--teal)"/>
    <polygon points="100,12.3 100,15 78,16.7" fill="var(--teal)"/>
    <polygon points="0,25 100,14.6 100,16.4 0,26.3" fill="var(--orange)"/>
    <polygon points="0,26.3 100,16.4 100,17 0,28" fill="var(--grey)"/>
  </svg>
  <div class="band"></div>
  <p class="site">harbortotalrecovery.com</p>
  <div class="dashes"><span></span><span></span><span></span></div>
</section>

</body>
</html>
```